Company director needs a business card design

I am a semi-retired former senior finance executive who sits on a number of public and private company boards and do some consulting work. I work largely with emerging businesses but deal regularly with top end of town lawyers, bankers etc. I need a thoughtful but relatively conservative design which would also resonate with my younger client base. Some colour would be good. Information limited to name, address, office tel, mobile and email.

Industry/Entity Type

Finance

```html
<!DOCTYPE html>
<html lang="en">
<head>
<meta charset="utf-8">
<title>Daniel Whitmore – Business Card</title>
<link rel="stylesheet" href="https://fonts.googleapis.com/css2?family=Source+Sans+3:wght@400;700&display=swap">
<style>
  :root {
    --backdrop: #d9dadc;
    --card-white: #ffffff;
    --ink: #0b0b0b;
    --night: #000000;
    --ocean: #1166a6;
    --sand: #ecdb80;
    --contact-text: #ffffff;
    --icon-fill: #ffffff;
    --icon-glyph: #1a6fb0;
  }
  * { margin: 0; padding: 0; box-sizing: border-box; }
  html, body {
    width: 1200px;
    height: 1200px;
    overflow: hidden;
    background: var(--backdrop);
  }
  .card {
    position: absolute;
    left: 100px;
    top: 298px;
    width: 1000px;
    height: 604px;
    background: var(--card-white);
    overflow: hidden;
    font-family: "Source Sans 3", "Myriad Pro", Arial, sans-serif;
  }
  .accent-panel {
    position: absolute;
    top: 0;
    right: 0;
    width: 500px;
    height: 100%;
    background: linear-gradient(100deg, var(--ocean) 0%, #0a3559 45%, var(--night) 80%);
  }
  .holder-name {
    position: absolute;
    left: 70px;
    top: 128px;
    font-size: 56px;
    font-weight: 700;
    letter-spacing: -0.5px;
    color: var(--ink);
    line-height: 1;
  }
  .contact-list {
    position: absolute;
    right: 53px;
    top: 406px;
    list-style: none;
  }
  .contact-item {
    display: flex;
    justify-content: flex-end;
    align-items: center;
    height: 35.5px;
    gap: 14px;
    color: var(--contact-text);
    font-size: 24px;
    font-weight: 400;
    line-height: 1;
    white-space: nowrap;
  }
  .contact-icon {
    width: 27px;
    height: 27px;
    flex: none;
  }
  .contact-icon .disc { fill: var(--icon-fill); }
  .contact-icon .glyph { fill: var(--icon-glyph); }
</style>
</head>
<body>
  <div class="card">
    <div class="accent-panel" role="img" aria-label="Decorative curved band graphic in blue, sand and black"></div>

    <h1 class="holder-name">Daniel Whitmore</h1>

    <ul class="contact-list">
      <li class="contact-item">
        <span>02 9412 5830</span>
        <svg class="contact-icon" viewBox="0 0 24 24" aria-label="Office phone">
          <circle class="disc" cx="12" cy="12" r="12"/>
          <path class="glyph" d="M8.2 5.5l2.2 2.6-1.3 1.6c.9 2 2.4 3.6 4.4 4.6l1.6-1.3 2.6 2.2-1.4 2.3c-5.2-.6-9.5-4.9-10.1-10.1z"/>
        </svg>
      </li>
      <li class="contact-item">
        <span>0432 718 205</span>
        <svg class="contact-icon" viewBox="0 0 24 24" aria-label="Mobile">
          <circle class="disc" cx="12" cy="12" r="12"/>
          <path class="glyph" d="M8.5 4.5h7a1 1 0 0 1 1 1v13a1 1 0 0 1-1 1h-7a1 1 0 0 1-1-1v-13a1 1 0 0 1 1-1zm.6 2v9h5.8v-9zm2.9 10.3a.9.9 0 1 0 0 1.8.9.9 0 0 0 0-1.8z"/>
        </svg>
      </li>
      <li class="contact-item">
        <span>daniel_whitmore@mailhub.net.au</span>
        <svg class="contact-icon" viewBox="0 0 24 24" aria-label="Email">
          <circle class="disc" cx="12" cy="12" r="12"/>
          <path class="glyph" d="M5 7.5h14v9H5zm1.4 1.2v.3L12 13l5.6-4v-.3zm0 1.8v4.8h11.2v-4.8L12 14.5z"/>
        </svg>
      </li>
      <li class="contact-item">
        <span>18 Carrow Street, Dee Why NSW 2099</span>
        <svg class="contact-icon" viewBox="0 0 24 24" aria-label="Address">
          <circle class="disc" cx="12" cy="12" r="12"/>
          <path class="glyph" d="M12 5.5l7 6h-2v6.5h-3.5v-4h-3v4H7v-6.5H5z"/>
        </svg>
      </li>
    </ul>
  </div>
</body>
</html>
```